Cap Horizon WEB Brindleton Pageo ebook cover (2nd of book series) *

Book Title :
Cap Horizon pour bâtir votre Présence Durable WEB

Or alternatively if design is better :
WEB : Cap Horizon pour bâtir votre Présence Durable

Subtitle : Pourquoi hisser votre page au sommet des listes du grand réseau

Subject : The book is a very practical how-to guide to help anyone increase dramatically their trafic through SEO (Search Engine Opimization)

It is written in French : so please keep punctuation as provided

The book cover MUST STAND OUT on the Brindleton Plateform as a small Thumbnail (The important words must be readable even at that size : CAP HORIZON, Référencement Naturel, SEO) as well as a 6*9 book.

The imagery should make the viewer feel that the book (and the author) are the authority in Search Engine Optimization and Digital Marketing

The readers should feel that they must have this book to increase their site or blog traffic fast.

It is most important that the book “pops off the shelf” and catches the eye quickly. The most important part of the design is that it sells, not that it looks pretty (but it can :-)

Important thing : this cover and ebook is part of a series of books all titled “Cap Horizon blablabla”. There is already one book of this series published (see cover 5) : Cap Horizon pour Doubler vos Gains. It’s important that at least one element of this new design recalls the design of the Cover 5 It can be for example the typo for the “7” being the same, or any other idea so that when someone sees both covers, they understand they are from the same series.

I have also enclosed my attempt so that you get the idea I am after, but don’t be too close to it. I am not a designer and I know it is bad, so be free, it is just here to explain the idea of the book cover.
Attached are some covers :
 Covers 1 to 4 are covers I like very much
 Cover 5 is from The first book of the Series : “Cap Horizon pour Doubler vos Gains” : there should be at least ONE (even tiny) element in common with the new design so that it’s clear they belong to the same series
 Cover 6 is my ugly attempt so that the idea is clear (hopefully)

Target Market(s)

Small entrepreneurs bloggers

Font styles to use
Sans Serif

Colors

Designer to choose colors to be used in the design.

Requirements
Must have
• The book cover MUST STAND OUT on the Brindleton Plateform as a small Thumbnail (The important must be readable even at that size : CAP HORIZON, Référencement Naturel, SEO) as well as a 6*9 book.
• Important thing : this cover and ebook is part of a series of books all titled “Cap Horizon blablabla”. There is already one book of this series published (see cover 5) : Cap Horizon pour Doubler vos Gains. It’s important that at least one element of this new design recalls the design of the Cover 5 It can be for example the typo for the “7” being the same, or any other idea so that when someone sees both covers, they understand they are from the same series.
• All the texts provided on the brief and my sample cover (6th cover mockup)
• Please enclose the text :
• Checklist SEO Incluse
• In a sticker (see last image as example)
Nice to have
• Nice and simple imagery. Like the one on Fold Levers. Very simple but also very powerful and meaningful
Should not have
• It should not be as cluttered as my attempt (6th cover enclosed)

```html
<!DOCTYPE html>
<html lang="fr">
<head>
<meta charset="utf-8">
<title>Cap Horizon pour bâtir votre Présence Durable</title>
<link rel="stylesheet" href="https://fonts.googleapis.com/css2?family=Bebas+Neue&family=Roboto+Condensed:wght@700&display=swap">
<style>
  :root {
    --orange: #f78b24;
    --navy: #0b4f7c;
    --paper: #ffffff;
    --gold: #ffc400;
    --gold-light: #ffe566;
    --chart-red: #d7261e;
    --band-text: #ffffff;
  }
  * { margin: 0; padding: 0; box-sizing: border-box; }
  html, body { width: 857px; height: 1200px; overflow: hidden; background: var(--paper); }
  .cover {
    position: relative;
    width: 857px;
    height: 1200px;
    background: var(--paper);
    font-family: "Bebas Neue", "Oswald", sans-serif;
    overflow: hidden;
  }
  .series-mark { position: absolute; left: 0; top: 0; }
  .title-line {
    position: absolute;
    left: 0;
    width: 100%;
    text-align: center;
    line-height: 1;
    white-space: nowrap;
  }
  .series-word {
    top: 74px;
    font-size: 178px;
    color: var(--orange);
    letter-spacing: 2px;
  }
  .headline {
    top: 282px;
    font-size: 182px;
    color: var(--orange);
    letter-spacing: 6px;
  }
  .connector {
    top: 437px;
    font-size: 46px;
    color: var(--navy);
  }
  .connector-verb {
    top: 483px;
    font-size: 64px;
    color: var(--navy);
  }
  .connector-verb .accent { color: var(--orange); }
  .main-topic {
    top: 560px;
    font-size: 158px;
    color: var(--navy);
    letter-spacing: 4px;
  }
  .main-topic-second {
    top: 683px;
    font-size: 136px;
    color: var(--orange);
    letter-spacing: 3px;
  }
  .growth-chart { position: absolute; left: 330px; top: 770px; }
  .sticker { position: absolute; left: 72px; top: 755px; }
  .sticker-text {
    position: absolute;
    left: 72px;
    top: 755px;
    width: 216px;
    height: 216px;
    display: flex;
    flex-direction: column;
    align-items: center;
    justify-content: center;
    font-family: "Roboto Condensed", "Arial Narrow", sans-serif;
    font-weight: 700;
    color: var(--navy);
    line-height: 0.92;
    transform: rotate(-8deg);
  }
  .sticker-text .small { font-size: 33px; }
  .sticker-text .big { font-size: 74px; }
  .subtitle-band {
    position: absolute;
    left: 0;
    top: 1065px;
    width: 100%;
    height: 50px;
    background: var(--navy);
    color: var(--band-text);
    font-size: 27px;
    letter-spacing: 0.3px;
    text-align: center;
    line-height: 52px;
    white-space: nowrap;
  }
  .author {
    position: absolute;
    left: 0;
    top: 1132px;
    width: 100%;
    text-align: center;
    font-size: 40px;
    letter-spacing: 9px;
    color: var(--orange);
  }
</style>
</head>
<body>
<main class="cover">

  <svg class="series-mark" width="857" height="300" viewBox="0 0 857 300" aria-hidden="true">
    <ellipse cx="425" cy="160" rx="215" ry="107" fill="none" stroke="var(--navy)" stroke-width="4"/>
    <path d="M440 28 Q560 45 600 100" fill="none" stroke="var(--navy)" stroke-width="4" stroke-linecap="round"/>
  </svg>

  <h1>
    <span class="title-line series-word">CAP</span>
    <span class="title-line headline">HORIZON</span>
    <span class="title-line connector">POUR</span>
    <span class="title-line connector-verb"><span class="accent">BÂTIR</span> VOTRE</span>
    <span class="title-line main-topic">PRÉSENCE</span>
    <span class="title-line main-topic-second">DURABLE</span>
  </h1>

  <svg class="growth-chart" width="330" height="290" viewBox="0 0 330 290" aria-label="Graphique de croissance">
    <defs>
      <linearGradient id="bar" x1="0" y1="0" x2="1" y2="0">
        <stop offset="0" stop-color="#ff9a3c"/>
        <stop offset="0.55" stop-color="#f4561c"/>
        <stop offset="1" stop-color="#d9410f"/>
      </linearGradient>
    </defs>
    <g fill="url(#bar)">
      <rect x="20"  y="262" width="20" height="22"/>
      <rect x="46"  y="256" width="20" height="28"/>
      <rect x="72"  y="250" width="20" height="34"/>
      <rect x="98"  y="242" width="20" height="42"/>
      <rect x="124" y="232" width="20" height="52"/>
      <rect x="150" y="220" width="20" height="64"/>
      <rect x="176" y="204" width="20" height="80"/>
      <rect x="202" y="186" width="20" height="98"/>
      <rect x="228" y="166" width="20" height="118"/>
      <rect x="254" y="138" width="20" height="146"/>
      <rect x="280" y="100" width="20" height="184"/>
      <rect x="306" y="64"  width="20" height="220"/>
    </g>
    <path d="M10 250 Q200 215 265 60" fill="none" stroke="var(--chart-red)" stroke-width="6" stroke-linecap="round"/>
    <polygon points="278,22 284,76 252,60" fill="var(--chart-red)"/>
  </svg>

  <svg class="sticker" width="216" height="216" viewBox="0 0 216 216" aria-hidden="true">
    <defs>
      <radialGradient id="gold" cx="0.4" cy="0.35" r="0.7">
        <stop offset="0" stop-color="var(--gold-light)"/>
        <stop offset="1" stop-color="var(--gold)"/>
      </radialGradient>
    </defs>
    <g fill="url(#gold)">
      <rect x="33" y="33" width="150" height="150" transform="rotate(0 108 108)"/>
      <rect x="33" y="33" width="150" height="150" transform="rotate(15 108 108)"/>
      <rect x="33" y="33" width="150" height="150" transform="rotate(30 108 108)"/>
      <rect x="33" y="33" width="150" height="150" transform="rotate(45 108 108)"/>
      <rect x="33" y="33" width="150" height="150" transform="rotate(60 108 108)"/>
      <rect x="33" y="33" width="150" height="150" transform="rotate(75 108 108)"/>
    </g>
  </svg>
  <div class="sticker-text">
    <span class="small">Checklist</span>
    <span class="big">SEO</span>
    <span class="small">Incluse</span>
  </div>

  <p class="subtitle-band">POURQUOI HISSER VOTRE PAGE AU SOMMET DES LISTES DU GRAND RÉSEAU</p>
  <p class="author">LUCIEN MARVAUD</p>

</main>
</body>
</html>
```